Business Card Design Project

New Business Card design for Varodine Technology Ltd using new Logo and new Tagline for staffing company.

About us from our website - www.varodine.example:

VaroDine is a leading and recognized Electronic Entertainment, Workforce Augmentation, and Project Management solutions provider with clients in Electronic Entertainment, Legal, Technology, Government and other verticals that range in size from start up organizations to Zenlar 500 companies. VaroDine is certified as an 8(a) minority and woman owned enterprise, established in 1998.

Target Market(s)

Companies in Electronic Entertainment, Legal, Government and Technology

Industry/Entity Type

Business

Requirements
Must have
• Must include in small letters the following information on back:

Established in 1998
8(a)(w)(e), Cage #7KRT9, DUNS #462137580

Front should have the following:
Derek Holloway
Vice President
5820 Birchmont Road
Fallowby, FB 482917
555-318-2746 X 100
555-902-6613 Fax
555-318-2746 Toll Free
name@varodine.example

Our Tagline: Connect • Collaborate • Achieve

```html
<!DOCTYPE html>
<html lang="en">
<head>
<meta charset="utf-8">
<title>VaroDine Business Card – Front</title>
<link rel="stylesheet" href="https://fonts.googleapis.com/css2?family=Didact+Gothic&display=swap">
<style>
  :root {
    --page-bg: #ffffff;
    --label-ink: #1a1a1a;
    --card-bg: #1c1c1e;
    --card-edge: #141415;
    --text-light: #e4e4e4;
    --text-muted: #b9b9b9;
    --accent-blue: #2a5cab;
    --rule-gray: #8a8a8a;
  }
  * { margin: 0; padding: 0; box-sizing: border-box; }
  html, body {
    width: 1200px;
    height: 747px;
    overflow: hidden;
    background: var(--page-bg);
    font-family: "Didact Gothic", "Century Gothic", sans-serif;
  }
  .sheet { position: relative; width: 1200px; height: 747px; }
  .side-label {
    position: absolute;
    top: 2px; left: 0; width: 100%;
    text-align: center;
    font-size: 50px;
    color: var(--label-ink);
    letter-spacing: 1px;
  }
  .card {
    position: absolute;
    left: 12px; top: 110px;
    width: 1178px; height: 632px;
    background: var(--card-bg);
    border: 1px solid var(--card-edge);
    color: var(--text-light);
  }
  .brand {
    position: absolute;
    left: 88px; top: 70px;
    display: flex; align-items: center; gap: 14px;
  }
  .brand-dot {
    width: 34px; height: 34px;
    border-radius: 50%;
    background: var(--accent-blue);
  }
  .brand-name {
    font-size: 58px;
    color: #ffffff;
    letter-spacing: 0.5px;
  }
  .address {
    position: absolute;
    left: 66px; top: 186px;
    font-size: 30px;
    line-height: 44px;
    color: var(--text-light);
  }
  .identity {
    position: absolute;
    right: 110px; top: 120px;
    font-size: 40px;
    white-space: nowrap;
    padding-bottom: 4px;
    border-bottom: 3px solid var(--rule-gray);
  }
  .identity .divider { color: var(--rule-gray); padding: 0 6px; }
  .identity .title { color: var(--accent-blue); }
  .contact {
    position: absolute;
    right: 104px; top: 192px;
    text-align: right;
    font-size: 32px;
    line-height: 44px;
    white-space: nowrap;
  }
  .contact .key { color: var(--accent-blue); }
  .contact .value { color: var(--text-light); }
  .contact .email { margin-top: 10px; font-size: 31px; }
  .tagline {
    position: absolute;
    left: 0; width: 100%;
    top: 480px;
    text-align: center;
    font-size: 32px;
    font-variant: small-caps;
    letter-spacing: 3px;
    color: var(--text-light);
    word-spacing: 6px;
  }
  .tagline .bullet { padding: 0 10px; }
</style>
</head>
<body>
<div class="sheet">
  <div class="side-label">FRONT</div>
  <section class="card" aria-label="Business card front">
    <div class="brand">
      <span class="brand-dot"></span>
      <span class="brand-name">VaroDine</span>
    </div>

    <div class="address">
      <div>Fallowby, FB 482917</div>
      <div>555-318-2746 X 100</div>
    </div>

    <div class="identity">
      <span class="name">Derek Holloway</span><span class="divider">|</span><span class="title">Vice president</span>
    </div>

    <div class="contact">
      <div><span class="key">Fax:</span> <span class="value">555-902-6613</span></div>
      <div><span class="key">Toll Free:</span>&nbsp; <span class="value">555-318-2746</span></div>
      <div class="email"><span class="value">derekholloway</span><span class="key">@varodine.example</span></div>
    </div>

    <div class="tagline">Connect<span class="bullet">•</span>Collaborate<span class="bullet">•</span>Achieve</div>
  </section>
</div>
</body>
</html>
```